Banner for back of trucks

We make a product that is called "Brindo".
It attaches to the side of hay balers and automatically applies tags to bales as they are being made.
We require a simple / modern banner design that will be affixed to the back of hay trucks showing that the hay on board has been Marked by Brindo.
The banner will be 52x91cm (landscape)
The banner needs to say "Marked by Brindo" using the company logo.
It also needs the website "www.brindo.com.au" displayed.
We have attached an image of our logo, the product itself and the back of a truck it will be attached to for reference.

```html
<!DOCTYPE html>
<html lang="en">
<head>
<meta charset="utf-8">
<title>Marked by Brindo – truck banner</title>
<link rel="stylesheet" href="https://fonts.googleapis.com/css2?family=Jost:ital,wght@0,400;0,500;1,400;1,500&display=swap">
<style>
  :root {
    --bark: #574a3b;
    --amber: #f9ad45;
    --mist: #d7ddd7;
    --white: #ffffff;
  }
  * { margin: 0; padding: 0; box-sizing: border-box; }
  html, body {
    width: 1200px;
    height: 686px;
    overflow: hidden;
    background: var(--bark);
  }
  .banner {
    position: relative;
    width: 1200px;
    height: 686px;
    background: var(--bark);
    font-family: "Jost", "Futura", sans-serif;
  }
  .banner__frame {
    position: absolute;
    left: 0;
    top: 0;
  }
  .banner__headline {
    position: absolute;
    left: 100px;
    width: 1000px;
    top: 124px;
    text-align: center;
    font-style: italic;
    font-weight: 400;
    font-size: 106px;
    line-height: 1;
    letter-spacing: 0.055em;
    color: var(--mist);
    white-space: nowrap;
  }
  .banner__headline-accent {
    color: var(--amber);
    font-weight: 500;
  }
  .brand-name {
    position: absolute;
    left: 268px;
    width: 664px;
    top: 312px;
    height: 200px;
    display: flex;
    align-items: center;
    justify-content: center;
    font-weight: 500;
    font-size: 170px;
    line-height: 1;
    letter-spacing: 0.04em;
    color: var(--mist);
  }
  .banner__web {
    position: absolute;
    left: 0;
    width: 1200px;
    top: 556px;
    text-align: center;
    font-style: italic;
    font-weight: 400;
    font-size: 46px;
    line-height: 1;
    letter-spacing: 0.13em;
    color: var(--amber);
  }
</style>
</head>
<body>
  <main class="banner">
    <svg class="banner__frame" width="1200" height="686" viewBox="0 0 1200 686" aria-hidden="true">
      <g fill="none" stroke-width="5">
        <polyline points="631,65.5 83.5,65.5 83.5,623.5 631,623.5" stroke="var(--amber)"/>
        <polyline points="631,65.5 1115.5,65.5 1115.5,623.5 631,623.5" stroke="var(--white)"/>
      </g>
    </svg>

    <h1 class="banner__headline">Marked <span class="banner__headline-accent">by</span> Brindo</h1>

    <div class="brand-name">Brindo</div>

    <p class="banner__web">www.brindo.com.au</p>
  </main>
</body>
</html>
```